Velandre Jewellery Display Card

We are a jewellery manufacturer and need artwork for an A4 size strut card to advertise our new "Moonleaf Halo Charm "
In the attached files is a picture of the new pendant and artwork for our trademark "Velandre"
We also need to include the phrase " a treasure of the heart "
as part of the artwork.
The background colour should be predominately white

Target Market(s)

This product has been designed as a gift for Mothers as it has their children names
engraved on the pendant

Industry/Entity Type

Manufacturer

Font styles to use
Serif
Script

Colors
ffffff

Requirements
Must have
• Artwork should be simple and elegant , the predominant look in Australian jewellery stores which is where these display cards will be is white, bright and elegant

```html
<!DOCTYPE html>
<html lang="en">
<head>
<meta charset="utf-8">
<title>Velandre – Moonleaf Halo Charm Display Card</title>
<link href="https://fonts.googleapis.com/css2?family=Josefin+Sans:wght@300&family=Great+Vibes&display=swap" rel="stylesheet">
<style>
  :root {
    --page-bg: #e4e4e4;
    --card-white: #ffffff;
    --brand-grey: #8e9396;
    --line-grey: #c9c9c9;
    --pattern-grey: #dcdcdc;
    --pattern-light: #ececec;
    --metal-light: #f4f5f6;
    --metal-dark: #a9adb0;
  }
  * { margin: 0; padding: 0; box-sizing: border-box; }
  html, body {
    width: 1200px;
    height: 1000px;
    overflow: hidden;
    background: var(--page-bg);
  }
  .canvas {
    position: relative;
    width: 1200px;
    height: 1000px;
  }
  .display-card {
    position: absolute;
    left: 270px;
    top: 33px;
    width: 660px;
    height: 934px;
    background: var(--card-white);
    box-shadow: 0 4px 18px rgba(0,0,0,0.12);
    overflow: hidden;
  }
  .brand-band {
    position: absolute;
    left: 0; top: 0;
    width: 100%;
    height: 205px;
    display: flex;
    align-items: center;
    justify-content: center;
    border-bottom: 3px solid var(--line-grey);
  }
  .brand-name {
    font-family: "Josefin Sans", sans-serif;
    font-weight: 300;
    font-size: 84px;
    letter-spacing: 2px;
    color: var(--brand-grey);
    text-transform: uppercase;
    padding-top: 14px;
    white-space: nowrap;
  }
  .pattern-field {
    position: absolute;
    left: 0; top: 208px;
    width: 100%;
    height: 548px;
    background: radial-gradient(circle at 50% 50%, var(--pattern-light), var(--pattern-grey));
  }
  .heart-stage {
    position: absolute;
    left: 110px;
    top: 250px;
    width: 440px;
    height: 440px;
  }
  .heart-stage svg { display: block; }
  .pendant-photo {
    position: absolute;
    left: 130px;
    top: 120px;
    width: 180px;
    height: 220px;
    border-radius: 50% 50% 48% 48%;
    background: radial-gradient(circle at 40% 40%, var(--metal-light), var(--metal-dark));
  }
  .tagline-band {
    position: absolute;
    left: 0; bottom: 0;
    width: 100%;
    height: 178px;
    border-top: 3px solid var(--line-grey);
    display: flex;
    align-items: center;
    justify-content: center;
  }
  .tagline {
    font-family: "Great Vibes", cursive;
    font-weight: 400;
    font-size: 48px;
    color: var(--brand-grey);
    white-space: nowrap;
  }
</style>
</head>
<body>
<main class="canvas">
  <section class="display-card">
    <header class="brand-band">
      <h1 class="brand-name">Velandre</h1>
    </header>

    <div class="pattern-field" role="img" aria-label="Soft grey paisley and floral lace pattern"></div>

    <div class="heart-stage">
      <svg width="440" height="440" viewBox="0 0 440 440" aria-hidden="true">
        <path d="M220 415 C 140 350, 20 270, 20 150 C 20 75, 80 25, 140 25 C 180 25, 205 45, 220 75 C 235 45, 260 25, 300 25 C 360 25, 420 75, 420 150 C 420 270, 300 350, 220 415 Z"
              fill="var(--card-white)" style="filter: drop-shadow(0 3px 6px rgba(0,0,0,0.12));"/>
      </svg>
      <div class="pendant-photo" role="img" aria-label="Photo of the silver Moonleaf Halo Charm: a tree-of-life teardrop pendant within engraved name rings"></div>
    </div>

    <footer class="tagline-band">
      <p class="tagline">a treasure of the heart</p>
    </footer>
  </section>
</main>
</body>
</html>
```